Kelvoranet.com Webpage Design

Design Brief for kelvoranet.com (Copy of Brief also in attached Word file)

Name of Website- kelvoranet.com (existing logo and look & feel of website to be changed)

Logo - Finalised. The logo files are attached with the brief as “logo.jpeg”. The “Blue- Grey” version of the logo is for use on lighter backgrounds and the “Orange-White” version of the logo is for use on darker backgrounds. (A full Black version of the logo is also attached). Both versions may be used in different parts of the website. All attached files are in .png format.
Status - The website in functional and is undergoing user trials. However, we want to improve the look & feel of the website so at it seems
a. cotemporary,
b. Easy to Navigate
c. professional and
d. Vibrant.

Please visit ‘kelvoranet.com’ to check out the website and its functionalities – please use it only as a reference for the features & functions to be provided, however the designer should use a ‘Free Hand’ in designing the composition of various parts of the webpage without getting too influenced by the existing design

Objective of the Website ‘kelvoranet.com –
a. It is a portal focussed on listing of ‘Retail’ specific real-estate properties by developers, owners and realty brokers. The properties shall listed under the following four categories-
i. Retail Malls
ii. Shopping Complexes
iii. High-street shops
iv. Retail Warehouses
*refer kelvoranet.com for better clarity

b. The abovementioned properties shall be listed either for ‘Sale’ or ‘rent\lease’ or both

c. Users shall visit the site in case they wish to acquire a retail \ shop space either on ‘sale’ or ‘rent’. These Users would be able to specify the ‘Search Criteria’ through the tool-bars provided on the website – the ‘Search Criteria’ shall comprise of ‘Type of space category’, ‘City’, ‘Locality’, transaction type ie ‘Rent \ Sale’ and ‘Area Range’

d. The main revenue model for the website shall be listing fee ( or advertising charges ) payable by those listing their properties on the website.

Three Main Pages of Website (kelvoranet.com) that need to be designed -
a. Main Home Page (visit the web link - http://kelvoranet.com/ ) - The main home page has the “Search Toolbar” for specifying of Search Criteria by the User. It shall also have the following features & functions-
i. Main Advertising Banner
ii. Featured Projects
iii. New Launches
iv. Toolbar with buttons – ‘Advertise with Us’, ‘Listings Alert’, ‘Quorra Desk’, ‘Advertiser Login’

b. Property Listings Page (visit the web link - http://kelvoranet.com/gurgaon-in-india ) - The List of property options that match the Criteria specified by the ‘User’ get displayed on this page.

c. Property Detail Page - When the ‘User’ clicks on the “More….” Button on the ‘Property Listings Page’ (given in point b. above) the web page with the details of the property opens. (For Example – visit the web link - http://kelvoranet.com/dorvik-Shopping-Complex-dorvik-bellmoor-gurgaon-636 )

Note:- Please refer to attached ‘Shopping’ related images the designer may use them on the website to provide a look & feel of retail if required – either separately or rotate in a single window

Target Market(s)

Retailers & Investors looking for retail space, Real Estate Brokers, Developers

Industry/Entity Type

Advertising

Number of Pages Required

3 page

Requirements
Must have
• Refer to existing site kelvoranet.com -- all the existing functionalities are a must have.
Nice to have
• The Designer may use the retail related images on the website if required for making it more vibrant. Refer attached images Shopping(1-6).jpg

```html
<!DOCTYPE html>
<html lang="en">
<head>
<meta charset="utf-8">
<title>Kelvoranet.com – Home</title>
<link href="https://fonts.googleapis.com/css2?family=Arimo:wght@400;700&family=EB+Garamond:wght@400;600&family=Open+Sans:wght@400;600;700&display=swap" rel="stylesheet">
<style>
:root{
  --blue:#1b9be6;
  --blue-dark:#0f7fc8;
  --sky:#a9dcf8;
  --grey-panel:#dcdcdc;
  --card-foot:#f1f1f1;
  --ink:#333;
  --muted:#666;
  --dark:#2b2b2b;
  --white:#fff;
}
*{box-sizing:border-box;margin:0;padding:0}
html,body{width:675px;height:1200px;overflow:hidden;background:var(--white)}
body{position:relative;font-family:"Arimo",Arial,sans-serif;color:var(--ink)}
.abs{position:absolute}

/* hero */
.hero{left:0;top:0;width:675px;height:316px;
  background:
    radial-gradient(ellipse 90px 70px at 455px 205px,rgba(226,120,190,.85),rgba(226,120,190,0)),
    radial-gradient(ellipse 70px 60px at 490px 235px,rgba(120,190,90,.7),rgba(120,190,90,0)),
    radial-gradient(ellipse 60px 90px at 260px 170px,rgba(70,120,200,.75),rgba(70,120,200,0)),
    radial-gradient(ellipse 45px 70px at 190px 180px,rgba(200,60,60,.6),rgba(200,60,60,0)),
    radial-gradient(ellipse 50px 70px at 345px 200px,rgba(235,235,245,.6),rgba(235,235,245,0)),
    radial-gradient(ellipse 90px 60px at 560px 140px,rgba(230,190,130,.55),rgba(230,190,130,0)),
    radial-gradient(ellipse 120px 80px at 90px 160px,rgba(180,120,80,.5),rgba(180,120,80,0)),
    linear-gradient(180deg,#2a2420 0%,#5a4638 40%,#7a6050 62%,#4a3a30 85%,#2e2420 100%)}
.header-shade{left:0;top:0;width:675px;height:108px;background:rgba(20,18,16,.7)}
.cities{left:0;top:7px;width:675px;text-align:center;color:var(--white);font-size:8px}
.cities-rule{left:52px;top:21px;width:571px;height:1px;background:rgba(255,255,255,.25)}
.brand{left:52px;top:30px;display:flex;align-items:center;gap:5px}
.brand-dot{width:20px;height:20px;border-radius:50%;background:var(--blue)}
.brand-name{font-family:"Open Sans",sans-serif;font-weight:700;font-size:17px;color:var(--blue)}
.search-box{left:294px;top:36px;width:84px;height:16px;border:1px solid #ccc;background:#1e1c1a;color:#ddd;font-size:8px;font-weight:700;padding:3px 4px}
.search-box svg{position:absolute;right:3px;top:3px}
.auth{left:556px;top:34px;display:flex;font-family:"Open Sans",sans-serif;font-size:7px;font-weight:600}
.auth span{height:17px;line-height:17px;padding:0 7px;color:var(--white)}
.auth .signin{background:var(--blue)}
.auth .signup{background:#666}
.cart{left:578px;top:58px;color:var(--white);font-size:7px;font-weight:700;display:flex;gap:3px;align-items:center}
.nav-rule{left:52px;width:571px;height:2px;background:var(--white)}
.nav{left:52px;top:83px;display:flex;font-family:"Open Sans",sans-serif;font-size:8px;font-weight:700;color:var(--white)}
.nav a{color:inherit;text-decoration:none;margin-left:12px}
.nav a:first-child{color:var(--blue);margin-right:22px}
.nav a:nth-child(2),.nav a:nth-child(3){margin-right:26px}

/* search panel */
.finder{left:120px;top:286px;width:436px;height:74px;background:linear-gradient(180deg,#35a9ee,#1b8fd8);border-radius:2px}
.finder h2{position:absolute;left:0;top:9px;width:100%;text-align:center;font-family:"EB Garamond",serif;font-weight:400;font-size:14px;color:var(--white);letter-spacing:.5px}
.select{position:absolute;top:37px;width:58px;height:17px;background:var(--white);color:#aaa;font-size:8px;padding:3px 4px}
.select svg{position:absolute;right:4px;top:6px}
.range-title{position:absolute;left:232px;top:29px;font-size:8px;color:var(--white)}
.range-val{position:absolute;left:290px;top:34px;font-size:5px;color:var(--white)}
.range-track{position:absolute;left:234px;top:44px;width:100px;height:3px;background:var(--white)}
.range-fill{position:absolute;left:234px;top:44px;width:31px;height:3px;background:#7dc242}
.knob{position:absolute;top:41px;width:8px;height:8px;border-radius:50%;background:var(--white);border:1px solid #999}
.range-lo{position:absolute;left:234px;top:52px;font-size:5px;color:var(--white)}
.range-hi{position:absolute;left:252px;top:55px;font-size:5px;color:var(--white)}
.finder-btn{position:absolute;left:360px;top:37px;width:59px;height:17px;background:#7a7a7a;border:1px solid #aaa;color:var(--white);font-size:6px;font-weight:700;text-align:center;line-height:15px}

/* sections */
.section-head{font-weight:700;font-size:11.5px;color:var(--blue);top:377px}
.section-rule{top:394px;height:1px;background:#999}
.launch-panel{left:52px;top:406px;width:146px;height:314px;background:var(--sky)}
.projects-panel{left:210px;top:406px;width:413px;height:314px;background:var(--grey-panel)}
.loc{font-size:8.5px;color:var(--muted);white-space:nowrap}
.loc b{color:#333}
.loc-blue,.loc-blue b{color:var(--blue)}
.launch-cap{background:var(--card-foot);font-size:9px;color:#444;padding:5px 5px;height:20px}
.card-foot{background:var(--card-foot);height:20px;display:flex;align-items:center;padding:0 4px;gap:4px;font-size:8px;color:#666}
.card-foot .icons{color:#bbb;font-size:9px}
.card-foot .price{margin-left:auto}
.more-btn{left:58px;top:693px;width:49px;height:18px;background:var(--blue);color:var(--white);font-size:8px;line-height:18px;padding-left:6px}
.arrow-btn{top:694px;width:18px;height:16px;background:var(--blue)}
.view-btn{left:239px;top:459px;width:79px;height:22px;background:var(--white);border:1px solid #ccc;font-size:7px;text-align:center;line-height:20px;color:#444}

/* offers */
.offer{top:746px;width:272px;height:110px}
.offer-tag{position:absolute;left:6px;top:16px;padding:4px 11px;font-family:"EB Garamond",serif;font-size:9px;color:var(--white);letter-spacing:.3px}
.offer h3{position:absolute;left:6px;top:40px;font-family:"EB Garamond",serif;font-weight:600;font-size:13px;line-height:15px;color:var(--white);letter-spacing:.3px}
.offer p{position:absolute;left:6px;top:76px;width:262px;font-family:"EB Garamond",serif;font-weight:600;font-size:7px;line-height:9px;color:var(--white)}

/* band */
.band{left:0;top:882px;width:675px;height:119px;
  background:
    radial-gradient(ellipse 90px 70px at 470px 90px,rgba(20,70,130,.45),rgba(20,70,130,0)),
    radial-gradient(ellipse 80px 60px at 340px 100px,rgba(120,210,240,.55),rgba(120,210,240,0)),
    radial-gradient(ellipse 70px 60px at 580px 60px,rgba(30,90,150,.4),rgba(30,90,150,0)),
    linear-gradient(120deg,#3aa7e6,#5cb8ea 45%,#2f96d6)}
.band h2{position:absolute;left:0;top:16px;width:100%;text-align:center;font-family:"EB Garamond",serif;font-weight:400;font-size:20px;color:var(--white)}
.band h2 span{color:#1d3d5a;letter-spacing:.5px}
.band p{position:absolute;left:74px;top:47px;width:527px;text-align:center;font-family:"EB Garamond",serif;font-size:8px;line-height:9px;color:var(--white)}

/* footer columns */
.col-title{top:1012px;font-family:"Open Sans",sans-serif;font-weight:600;font-size:10.5px;color:#222}
.col-rule{top:1010px;width:1px;height:133px;background:#555}
.small{font-size:6px;line-height:10px;color:#333}
.field{background:#e6e6e6;border:1px solid #bbb;font-size:6px;color:#555;padding:3px 4px}
.dark-btn{background:#1e1e1e;color:var(--white);font-family:"Open Sans",sans-serif;font-weight:700;text-align:center;border-radius:2px}
.foot-line{left:0;top:1147px;width:675px;height:3px;background:var(--blue)}
.footer{left:0;top:1150px;width:675px;height:50px;background:var(--dark)}
.footer p{position:absolute;left:52px;font-size:6.5px;color:#ddd}
</style>
</head>
<body>

<!-- hero + header -->
<div class="abs hero" role="img" aria-label="Family walking through a shopping mall carrying colourful shopping bags"></div>
<div class="abs header-shade"></div>
<div class="abs cities">Bangalore | Chennai | Greater Noida | Gurgaon | Hyderabad | Jaipur | Khanna | Kolkatta | Mumbai | Noida | Pune | Surat</div>
<div class="abs cities-rule"></div>
<div class="abs brand"><span class="brand-dot"></span><span class="brand-name">kelvoranet</span></div>
<div class="abs search-box">Search
  <svg width="8" height="8" viewBox="0 0 8 8"><circle cx="3.2" cy="3.2" r="2.4" fill="none" stroke="#ddd" stroke-width="1.2"/><line x1="5" y1="5" x2="7.5" y2="7.5" stroke="#ddd" stroke-width="1.3"/></svg>
</div>
<div class="abs auth"><span class="signin">Sign in</span><span class="signup">Sign up</span></div>
<div class="abs cart">
  <svg width="9" height="8" viewBox="0 0 9 8"><path d="M0 1h1.6l1 4.2h4.6l1.2-3.2H2.3" fill="none" stroke="#fff" stroke-width="1"/><circle cx="3.2" cy="7" r=".8" fill="#fff"/><circle cx="6.6" cy="7" r=".8" fill="#fff"/></svg>
  CART &nbsp;(0)
</div>
<div class="abs nav-rule" style="top:74px"></div>
<nav class="abs nav">
  <a href="#">&#8962; Home</a><a href="#">Advertise With Us</a><a href="#">Quorra Desk</a><a href="#">Listing Alerts</a>
</nav>
<div class="abs nav-rule" style="top:100px"></div>

<!-- search finder -->
<div class="abs finder">
  <h2>FIND YOUR DREAM HOME TODAY</h2>
  <div class="select" style="left:22px">Type<svg width="6" height="4" viewBox="0 0 6 4"><path d="M0 0l3 4 3-4" fill="#999"/></svg></div>
  <div class="select" style="left:90px">shop<svg width="6" height="4" viewBox="0 0 6 4"><path d="M0 0l3 4 3-4" fill="#999"/></svg></div>
  <div class="select" style="left:157px">Hall<svg width="6" height="4" viewBox="0 0 6 4"><path d="M0 0l3 4 3-4" fill="#999"/></svg></div>
  <div class="range-title">Price Range</div>
  <div class="range-val">1,5000-5500,00</div>
  <div class="range-track"></div>
  <div class="range-fill"></div>
  <div class="knob" style="left:231px"></div>
  <div class="knob" style="left:262px"></div>
  <div class="range-lo">0</div>
  <div class="range-hi">80,000</div>
  <div class="finder-btn">SEARCH</div>
</div>

<!-- section headings -->
<div class="abs section-head" style="left:52px">Featured New Launches</div>
<div class="abs section-rule" style="left:52px;width:143px"></div>
<div class="abs section-head" style="left:210px">Featured Retail Projects</div>
<div class="abs section-rule" style="left:210px;width:413px"></div>

<!-- new launches -->
<div class="abs launch-panel"></div>
<div class="abs loc loc-blue" style="left:60px;top:414px">street 5, juhu mall,<b>wasington</b></div>
<div class="abs" style="left:58px;top:429px;width:132px;height:89px;background:radial-gradient(ellipse 50px 30px at 60px 60px,rgba(240,190,90,.8),rgba(240,190,90,0)),linear-gradient(180deg,#5a5a66 0%,#8a7a5a 50%,#c09a50 70%,#2a2a1a 100%)" role="img" aria-label="Hotel towers lit at dusk"></div>
<div class="abs launch-cap" style="left:58px;top:518px;width:132px">LOREM IPSUM</div>
<div class="abs loc loc-blue" style="left:60px;top:553px">street 5, juhu mall,<b>wasington</b></div>
<div class="abs" style="left:58px;top:568px;width:132px;height:90px;background:linear-gradient(180deg,#5a9ae0 0%,#8ab8e8 25%,#e0c48a 45%,#c8a070 75%,#7a6a4a 100%)" role="img" aria-label="Shopping arcade building with palm trees"></div>
<div class="abs launch-cap" style="left:58px;top:658px;width:132px">LOREM IPSUM</div>
<div class="abs more-btn">MORE &nbsp;&#8250;</div>

<!-- retail projects -->
<div class="abs projects-panel"></div>

<div class="abs loc" style="left:216px;top:413px">street 5, juhu mall,<b>wasington</b></div>
<div class="abs" style="left:214px;top:427px;width:128px;height:87px;background:radial-gradient(ellipse 40px 30px at 40px 70px,rgba(200,120,200,.6),rgba(200,120,200,0)),linear-gradient(160deg,#5ab0e0,#3a90c8 55%,#2a6a9a)" role="img" aria-label="Shopper browsing in a store, blue tint"></div>
<div class="abs view-btn">View The Listing</div>
<div class="abs card-foot" style="left:214px;top:514px;width:128px"><span class="icons">&#9825; &#9734;</span><span class="price">$ 10,000</span></div>

<div class="abs loc" style="left:353px;top:413px">street 5, juhu mall,<b>wasington</b></div>
<div class="abs" style="left:351px;top:427px;width:128px;height:87px;background:radial-gradient(ellipse 50px 35px at 60px 45px,rgba(220,210,255,.8),rgba(220,210,255,0)),radial-gradient(ellipse 30px 25px at 20px 25px,rgba(230,60,80,.6),rgba(230,60,80,0)),linear-gradient(170deg,#1a1a3a,#5a5aa0 50%,#2a2a4a)" role="img" aria-label="Glass mall facade lit at night"></div>
<div class="abs card-foot" style="left:351px;top:514px;width:128px"><span class="icons">&#9825; &#9734;</span><span class="price">$ 10,000</span></div>

<div class="abs loc" style="left:490px;top:413px">street 5, juhu mall,<b>wasington</b></div>
<div class="abs" style="left:488px;top:427px;width:128px;height:87px;background:radial-gradient(ellipse 40px 30px at 40px 50px,rgba(240,200,80,.7),rgba(240,200,80,0)),radial-gradient(ellipse 35px 30px at 95px 40px,rgba(80,160,240,.6),rgba(80,160,240,0)),linear-gradient(170deg,#0e0e1e,#4a3a6a 50%,#6a4a2a)" role="img" aria-label="Colourful mall exterior at night"></div>
<div class="abs card-foot" style="left:488px;top:514px;width:128px"><span class="icons">&#9825; &#9734;</span><span class="price">$ 10,000</span></div>

<div class="abs loc" style="left:216px;top:554px">street 5, juhu mall,<b>wasington</b></div>
<div class="abs" style="left:214px;top:569px;width:128px;height:86px;background:radial-gradient(ellipse 40px 20px at 60px 72px,rgba(240,190,110,.75),rgba(240,190,110,0)),linear-gradient(170deg,#14244a,#2a4a90 55%,#4a4a6a)" role="img" aria-label="High-rise retail towers at night"></div>
<div class="abs card-foot" style="left:214px;top:655px;width:128px"><span class="icons">&#9825; &#9734;</span><span class="price">$ 10,000</span></div>

<div class="abs loc" style="left:353px;top:554px">street 5, juhu mall,<b>wasington</b></div>
<div class="abs" style="left:351px;top:569px;width:128px;height:86px;background:radial-gradient(ellipse 40px 20px at 60px 72px,rgba(200,40,50,.55),rgba(200,40,50,0)),linear-gradient(180deg,#3a7ad0,#9ec4e8 40%,#b8b8c0 60%,#5a5a5e)" role="img" aria-label="Shopping centre with tower under blue sky"></div>
<div class="abs card-foot" style="left:351px;top:655px;width:128px"><span class="icons">&#9825; &#9734;</span><span class="price">$ 10,000</span></div>

<div class="abs loc" style="left:490px;top:554px">street 5, juhu mall,<b>wasington</b></div>
<div class="abs" style="left:488px;top:569px;width:128px;height:86px;background:radial-gradient(ellipse 45px 22px at 70px 62px,rgba(240,150,60,.7),rgba(240,150,60,0)),linear-gradient(180deg,#1a1a1e,#3a3036 55%,#6a4a30)" role="img" aria-label="Department store front at night"></div>
<div class="abs card-foot" style="left:488px;top:655px;width:128px"><span class="icons">&#9825; &#9734;</span><span class="price">$ 10,000</span></div>

<div class="abs arrow-btn" style="left:212px"><svg width="18" height="16" viewBox="0 0 18 16"><path d="M11 4l-4 4 4 4" fill="none" stroke="#fff" stroke-width="2"/></svg></div>
<div class="abs arrow-btn" style="left:232px"><svg width="18" height="16" viewBox="0 0 18 16"><path d="M7 4l4 4-4 4" fill="none" stroke="#fff" stroke-width="2"/></svg></div>

<!-- special offers -->
<div class="abs offer" style="left:52px;background:radial-gradient(ellipse 70px 40px at 200px 20px,rgba(170,180,150,.6),rgba(170,180,150,0)),linear-gradient(180deg,#7a7a6e,#4a4a42 55%,#2a2a28)" role="img" aria-label="Shopping street with residential towers">
  <div class="offer-tag" style="background:#2a2a2a">SPECIAL OFFER</div>
  <h3>LOREM IPSUM DOLOR<br>SIT AMET</h3>
  <p>Est nonummy nisl suscipit praesent suspendisse sem, proident fer-<br>mentum dolorem gravida suscipit volutpat, non at ante ac</p>
</div>
<div class="abs offer" style="left:351px;background:radial-gradient(ellipse 60px 30px at 200px 60px,rgba(90,110,170,.6),rgba(90,110,170,0)),linear-gradient(180deg,#1a1a22,#3a3a4a 55%,#1e1e26)" role="img" aria-label="Modern mall building at night">
  <div class="offer-tag" style="background:var(--blue)">SPECIAL OFFER</div>
  <h3>LOREM IPSUM DOLOR<br>SIT AMET</h3>
  <p>Est nonummy nisl suscipit praesent suspendisse sem, proident fer-<br>mentum dolorem gravida suscipit volutpat, non at ante ac</p>
</div>

<!-- promo band -->
<div class="abs band" role="img" aria-label="Blue-tinted shopper carrying shopping bags">
  <h2>The greatest shops for <span>KELVORANET</span></h2>
  <p>Lorem ipsum dolor sit amet, quisquam suspendisse varius nec, enim eget quis quam integer porttitor rutrum, quis interdum aliquam donec sollicitudin per, orci vel posuere elit ac enim, dolor elit eu. Suscipit sem in.</p>
</div>

<!-- footer columns -->
<div class="abs col-title" style="left:96px">Listing Alert</div>
<svg class="abs" style="left:95px;top:1031px" width="31" height="32" viewBox="0 0 31 32"><rect x="1" y="10" width="29" height="21" fill="#1d3d5a"/><path d="M1 10l14.5-9 14.5 9" fill="#2a5a80"/><rect x="6" y="5" width="19" height="17" fill="#fff"/><path d="M1 31l14.5-11 14.5 11" fill="#2a5a80"/><text x="15.5" y="17" text-anchor="middle" font-family="Arial,sans-serif" font-size="10" font-weight="700" fill="#1d3d5a">@</text></svg>
<div class="abs small" style="left:132px;top:1037px;width:96px">Suscribe for Fortnightly Email update on New Listings @ Kelvoranet</div>
<div class="abs small" style="left:99px;top:1075px;color:#888">Email Your Email Address:</div>
<div class="abs dark-btn" style="left:168px;top:1099px;width:53px;height:18px;font-size:9px;line-height:18px">Subscribe</div>

<div class="abs col-rule" style="left:233px"></div>
<div class="abs col-title" style="left:249px">Editor's Choice</div>
<div class="abs small" style="left:249px;top:1037px;width:178px">A “Select” Listing of Retail Properties Handpicked by our Editors based on their own positive evaluation on param-eters &amp; attributes such as Design Concept, Location, Developer, Success Potential. So Read On to Check Out for yourself ............ ..</div>
<div class="abs col-rule" style="left:441px"></div>

<div class="abs col-title" style="left:472px">Quorra Desk</div>
<div class="abs field" style="left:472px;top:1038px;width:136px;height:15px">Email Your Email Address:</div>
<div class="abs field" style="left:472px;top:1063px;width:136px;height:29px">Add Description of Requirement</div>
<div class="abs dark-btn" style="left:555px;top:1099px;width:53px;height:18px;font-size:10px;line-height:18px">Send</div>

<div class="abs foot-line"></div>
<footer class="abs footer">
  <p style="top:15px">Copyright © 2013 Marlow Retail Hub.com. All rights reserved.</p>
  <p style="top:28px">website by Tessadyne Labs.</p>
  <div class="abs brand" style="left:484px;top:12px"><span class="brand-dot"></span><span class="brand-name">kelvoranet</span></div>
</footer>

</body>
</html>
```